TIDAL VERGE needs bisness cards pronto

Bisness name is "TIDAL VERGE" new bisness the bisness includes lawn mowing, garden matanace, and any jobs around the house.
I need a card that is colorful and vibrant and the bisness of lawn mowing maybe with some nature with it. It also needs my contact details"Darren Quellby mobile 0413562049 call for free quote and email norma.vance@fernmail.com.au and a catchy tag line

Industry/Entity Type

House

Requirements
Must have
• Bisness name "TIDAL VERGE"
Contact details "0413562049"
Email norma.vance@fernmail.com.au
Call for free quote

```html
<!DOCTYPE html>
<html lang="en">
<head>
<meta charset="utf-8">
<title>Tidal Verge – Business Card</title>
<link rel="stylesheet" href="https://fonts.googleapis.com/css2?family=Bebas+Neue&display=swap">
<style>
  :root {
    --backdrop: #000000;
    --green-start: #7cc693;
    --green-end: #a3d3a1;
    --panel-white: #ffffff;
    --ink-grey: #676767;
    --text-white: #ffffff;
  }
  html, body {
    margin: 0;
    padding: 0;
    width: 1200px;
    height: 1000px;
    overflow: hidden;
    background: var(--backdrop);
  }
  .card {
    position: absolute;
    left: 75px;
    top: 201px;
    width: 1050px;
    height: 600px;
    overflow: hidden;
    background: linear-gradient(150deg, var(--green-start) 0%, var(--green-start) 30%, var(--green-end) 100%);
    font-family: "Bebas Neue", "Oswald", sans-serif;
    line-height: 1;
  }
  .quote-panel {
    position: absolute;
    left: 0;
    top: 0;
    width: 400px;
    height: 370px;
  }
  .cta-call {
    position: absolute;
    left: 46px;
    top: 99px;
    font-size: 97px;
    color: var(--ink-grey);
    margin: 0;
  }
  .cta-detail {
    position: absolute;
    left: 194px;
    font-size: 42px;
    color: var(--ink-grey);
    margin: 0;
  }
  .cta-detail--first { top: 108px; }
  .cta-detail--second { top: 138px; }
  .brand {
    position: absolute;
    left: 588px;
    top: 65px;
    width: 400px;
  }
  .brand-name {
    margin: 0;
    font-size: 80px;
    color: var(--text-white);
    letter-spacing: 3px;
    text-align: center;
    white-space: nowrap;
  }
  .brand-rule {
    position: absolute;
    left: 0;
    top: 76px;
    width: 400px;
    height: 3px;
    background: var(--text-white);
  }
  .brand-owner {
    position: absolute;
    left: 0;
    top: 77px;
    width: 400px;
    margin: 0;
    font-size: 26px;
    color: var(--ink-grey);
    letter-spacing: 9px;
    text-align: center;
    white-space: nowrap;
  }
  .contact-marker {
    position: absolute;
    background: var(--panel-white);
  }
  .contact-marker--phone {
    left: 0;
    top: 428px;
    width: 47px;
    height: 39px;
  }
  .contact-marker--email {
    right: 0;
    top: 504px;
    width: 45px;
    height: 28px;
  }
  .contact-phone {
    position: absolute;
    left: 70px;
    top: 420px;
    margin: 0;
    font-size: 57px;
    color: var(--text-white);
    letter-spacing: 1px;
  }
  .contact-email {
    position: absolute;
    right: 60px;
    top: 498px;
    margin: 0;
    font-size: 43px;
    color: var(--text-white);
    white-space: nowrap;
  }
</style>
</head>
<body>
  <main class="card">
    <svg class="quote-panel" viewBox="0 0 400 370" aria-hidden="true">
      <polygon points="0,0 370,0 391,212 178,365 0,287" fill="var(--panel-white)"/>
    </svg>

    <p class="cta-call">Call</p>
    <p class="cta-detail cta-detail--first">For Free</p>
    <p class="cta-detail cta-detail--second">Quote</p>

    <div class="brand">
      <h1 class="brand-name">TIDAL VERGE</h1>
      <div class="brand-rule"></div>
      <p class="brand-owner">DARREN QUELLBY</p>
    </div>

    <div class="contact-marker contact-marker--phone"></div>
    <p class="contact-phone">0413562049</p>

    <p class="contact-email">NORMA.VANCE@FERNMAIL.COM.AU</p>
    <div class="contact-marker contact-marker--email"></div>
  </main>
</body>
</html>
```